Business Card for innovative, tech/consultant company

We are specializing in bringing together Efficiency methodology and Technology for our Business customers. We would like an astonishing business Card that matches this idea.

Target Market(s)

Businesses of medium size or more

Industry/Entity Type

Business Consultant

Contact Information for Business Card

Name, Title, personal email, www, address, phone

Font styles to use
Sans Serif

Colors
3277b5

Requirements
Must have
• - innovative, efficient design
• - good readable
• - Colors must match our logo (blue and grey)
• - the attached font (is licensed by our Company) must be used (Syntax LT)
Should not have
• overloaded

```html
<!DOCTYPE html>
<html lang="en">
<head>
<meta charset="utf-8">
<title>Veralink Business Card</title>
<link href="https://fonts.googleapis.com/css2?family=Open+Sans:wght@400;500&display=swap" rel="stylesheet">
<style>
  :root {
    --backdrop: #b4b4b4;
    --card: #efeeec;
    --card-shade: #e6e5e3;
    --brand-blue: #0a80c6;
    --brand-grey: #77767a;
    --ink: #2e2e30;
  }
  * { box-sizing: border-box; margin: 0; padding: 0; }
  html, body {
    width: 1200px;
    height: 936px;
    overflow: hidden;
    background: var(--backdrop);
    font-family: "Open Sans", sans-serif;
  }
  .business-card {
    position: absolute;
    left: 50px;
    top: 150px;
    width: 1100px;
    height: 637px;
    background: var(--card);
    overflow: hidden;
  }
  .network-backdrop {
    position: absolute;
    inset: 0;
    background: linear-gradient(135deg, var(--card) 0%, var(--card-shade) 50%, var(--card) 100%);
  }
  .brand-name {
    position: absolute;
    left: 176px;
    top: 128px;
    font-size: 90px;
    font-weight: 400;
    line-height: 1;
    color: var(--brand-grey);
    letter-spacing: 1px;
  }
  .contact-item {
    position: absolute;
    top: 377px;
    display: flex;
    align-items: center;
    gap: 32px;
  }
  .contact-item.phone { left: 55px; }
  .contact-item.web { left: 360px; }
  .contact-item.location { left: 676px; }
  .contact-icon {
    width: 55px;
    height: 55px;
    border-radius: 8px;
    background: var(--brand-blue);
    display: flex;
    align-items: center;
    justify-content: center;
    flex-shrink: 0;
  }
  .contact-icon svg { width: 34px; height: 34px; }
  .contact-lines {
    font-size: 18px;
    line-height: 27px;
    letter-spacing: 2px;
    color: var(--ink);
    white-space: nowrap;
  }
  .accent-band {
    position: absolute;
    left: 4px;
    right: 4px;
    top: 496px;
    height: 21px;
    background: var(--brand-blue);
  }
</style>
</head>
<body>
  <main class="business-card">
    <div class="network-backdrop" role="img" aria-label="Faint connected-node network pattern in light grey"></div>

    <h1 class="brand-name">Veralink</h1>

    <div class="contact-item phone">
      <div class="contact-icon">
        <svg viewBox="0 0 24 24" aria-hidden="true">
          <path fill="#fff" d="M6.6 3.2c.5-.3 1.1-.2 1.4.3l2 3c.3.5.2 1.1-.2 1.4l-1.4 1.1c.9 2 2.5 3.6 4.5 4.5l1.1-1.4c.3-.4 1-.5 1.4-.2l3 2c.5.3.6.9.3 1.4l-1.2 2c-.5.8-1.5 1.2-2.4.9C9.6 16.5 7.5 14.4 5.8 8.7c-.3-.9.1-1.9.9-2.4z"/>
        </svg>
      </div>
      <div class="contact-lines">
        <p>+213 555 014 2290</p>
        <p>+213 555 014 2290</p>
      </div>
    </div>

    <div class="contact-item web">
      <div class="contact-icon">
        <svg viewBox="0 0 24 24" aria-hidden="true" fill="none" stroke="#fff" stroke-width="1.6">
          <circle cx="12" cy="12" r="9"/>
          <ellipse cx="12" cy="12" rx="4" ry="9"/>
          <line x1="3" y1="12" x2="21" y2="12"/>
          <path d="M4.5 7.5h15M4.5 16.5h15"/>
        </svg>
      </div>
      <div class="contact-lines">
        <p>info@veralink.com</p>
        <p>www.veralink.com</p>
      </div>
    </div>

    <div class="contact-item location">
      <div class="contact-icon">
        <svg viewBox="0 0 24 24" aria-hidden="true">
          <path fill="#fff" fill-rule="evenodd" d="M12 2a7 7 0 0 1 7 7c0 5-7 13-7 13S5 14 5 9a7 7 0 0 1 7-7zm0 4a3 3 0 1 0 0 6 3 3 0 0 0 0-6z"/>
        </svg>
      </div>
      <div class="contact-lines">
        <p>Site Adress</p>
        <p>ELM AVENUE, NY CITY, USA</p>
      </div>
    </div>

    <div class="accent-band"></div>
  </main>
</body>
</html>
```